Musician website

I need a website developed for a musician

The style and content of the website were are looking for is like :

https://www.corvantellisounds.example/
https://www.grindolax.example/
https://www.mirelwandby.example/
https://www.olbrenquist.example/?frontpage=true

The name of the musician is 'Tamsin Orlebo'

Attached are some professional photos to use

Number of Pages Required

1 page

```html
<!DOCTYPE html>
<html lang="en">
<head>
<meta charset="utf-8">
<title>Tamsin Orlebo — Official Site</title>
<link rel="stylesheet" href="https://fonts.googleapis.com/css2?family=Oswald:wght@400;500;700&family=Montserrat:wght@400;500;600&display=swap">
<style>
:root{
  --ink:#1d1d1d;
  --muted:#6b6b6b;
  --ghost:#e6e6e6;
  --accent:#e8471c;
  --news-bg:#f3f3f3;
  --white:#ffffff;
  --line:#cfcfcf;
  --merch-fill:#eeeeee;
}
*{box-sizing:border-box;margin:0;padding:0}
html,body{width:1200px;height:4882px;overflow:hidden;background:var(--white)}
body{position:relative;font-family:"Montserrat",sans-serif;color:var(--ink)}
.abs{position:absolute}
.heading{font-family:"Oswald",sans-serif;font-weight:500;font-size:36px;letter-spacing:.5px;text-transform:uppercase;text-align:center;left:0;width:1200px}
.ghost-word{position:absolute;font-family:"Oswald",sans-serif;font-weight:700;text-transform:uppercase;color:var(--ghost);white-space:nowrap;line-height:1;transform-origin:left top;transform:rotate(-90deg)}
.btn{position:absolute;display:flex;align-items:center;justify-content:center;border:1.5px solid var(--ink);font-family:"Oswald",sans-serif;font-weight:500;font-size:18px;text-transform:uppercase;color:var(--ink);background:var(--white);white-space:nowrap}
.photo{position:absolute}

/* hero */
.hero{position:absolute;left:0;top:0;width:1200px;height:738px;overflow:hidden;background:linear-gradient(180deg,#3a3d35 0%,#4b4f44 35%,#3c3c38 70%,#2b2b28 100%)}
.hero-nav{position:absolute;top:36px;left:0;width:1200px;height:24px}
.hero-nav span{position:absolute;font-family:"Oswald",sans-serif;font-size:16px;color:var(--white);text-transform:uppercase}
.social{position:absolute;left:1131px;width:36px;height:36px;border-radius:50%;background:#1a1a1a}
.hero-name{position:absolute;left:-6px;top:528px;font-family:"Oswald",sans-serif;font-weight:700;font-size:232px;line-height:1;color:var(--accent);letter-spacing:-2px;white-space:nowrap}

/* music */
.arrow{position:absolute;width:24px;height:32px}
.music-date{top:1326px;left:0;width:1200px;text-align:center;font-size:17px;font-weight:500}
.music-title{top:1358px;left:0;width:1200px;text-align:center;font-size:30px;font-weight:600}

/* videos */
.videos{position:absolute;left:0;top:1580px;width:1200px;height:743px;overflow:hidden;background:linear-gradient(90deg,#d8d8d8,#e6e6e6 50%,#dcdcdc)}
.dot{position:absolute;top:2233px;width:12px;height:12px;border-radius:50%;border:1.5px solid #444}

/* tours */
.tour-text{top:2492px;left:110px;width:380px;font-size:15px;line-height:27.5px;color:var(--muted)}
.tour-title{position:absolute;left:770px;font-size:21px;font-weight:500}
.tour-meta{position:absolute;left:770px;font-size:15px;color:var(--muted);display:flex;align-items:center;gap:4px}
.view-all{top:2912px;left:770px;font-family:"Oswald",sans-serif;font-weight:500;font-size:18px;text-decoration:underline;text-transform:uppercase}

/* news */
.news{position:absolute;left:0;top:3015px;width:1200px;height:682px;background:var(--news-bg);overflow:hidden}
.news-title{position:absolute;font-family:"Oswald",sans-serif;font-weight:400;font-size:20px;line-height:29px;width:300px}
.news-date{position:absolute;font-size:15px;color:var(--muted)}

/* merch */
.merch-box{position:absolute;top:3866px;width:232px;height:254px;border:1.5px solid var(--line);background:var(--white);padding:14px}
.merch-photo{width:100%;height:100%;background:linear-gradient(180deg,#f4f4f4,#e4e4e4)}
.merch-name{position:absolute;top:4143px;width:232px;text-align:center;font-size:21px;font-weight:500;color:#333}
.merch-price{position:absolute;top:4184px;width:232px;text-align:center;font-size:15px;color:var(--muted)}

/* newsletter */
.newsletter{position:absolute;left:0;top:4418px;width:1200px;height:373px;background:linear-gradient(180deg,#303030,#1f1f1f);overflow:hidden}
.field{position:absolute;font-size:15px;color:#d8d8d8;border-bottom:1.5px solid #8a8a8a;height:38px;padding-top:4px}
.footer{position:absolute;top:4825px;left:0;width:1200px;text-align:center;font-size:15px;color:var(--muted)}
</style>
</head>
<body>

<!-- HERO -->
<header class="hero" role="img" aria-label="Portrait of the musician among large dark boulders and greenery">
  <nav class="hero-nav">
    <span style="left:748px">Music</span>
    <span style="left:844px">Videos</span>
    <span style="left:946px">Photos</span>
    <span style="left:1052px">News</span>
  </nav>
  <div class="social" style="top:236px"></div>
  <div class="social" style="top:289px"></div>
  <div class="social" style="top:342px"></div>
  <div class="social" style="top:395px"></div>
  <div class="social" style="top:448px"></div>
  <div class="social" style="top:501px"></div>
  <div class="social" style="top:554px"></div>
  <div class="social" style="top:607px"></div>
  <div class="hero-name">TAMSIN</div>
</header>

<!-- MUSIC -->
<section>
  <h2 class="heading abs" style="top:820px">Music</h2>
  <div class="photo" style="left:406px;top:900px;width:388px;height:380px;background:linear-gradient(180deg,#4f6b3f,#6d6a60 55%,#5a5650)" role="img" aria-label="Album cover: musician seated on stone steps with guitar, titled Tamsin Orlebo"></div>
  <svg class="arrow" style="left:352px;top:1074px" viewBox="0 0 24 32"><path d="M16 4 L6 16 L16 28" fill="none" stroke="#333" stroke-width="2.5"/></svg>
  <svg class="arrow" style="left:823px;top:1074px" viewBox="0 0 24 32"><path d="M8 4 L18 16 L8 28" fill="none" stroke="#333" stroke-width="2.5"/></svg>
  <div class="ghost-word" style="left:855px;top:1282px;font-size:150px">Music</div>
  <div class="abs music-date">
    <svg width="16" height="15" viewBox="0 0 16 15" style="vertical-align:-2px"><rect x="1" y="2" width="14" height="12" fill="none" stroke="#555" stroke-width="1.6"/><rect x="1" y="2" width="14" height="3" fill="#555"/></svg>
    MAR 25TH, 2021
  </div>
  <div class="abs music-title">Voluptatem accusaum doloremque laudan</div>
  <div class="btn" style="left:502px;top:1426px;width:194px;height:59px">Stream/Download</div>
</section>

<!-- VIDEOS -->
<section class="videos">
  <div class="ghost-word" style="left:126px;top:592px;font-size:150px;color:#f3f3f3">Videos</div>
</section>
<h2 class="heading abs" style="top:1663px">Videos</h2>
<div class="photo" style="left:294px;top:1763px;width:612px;height:429px;background:linear-gradient(90deg,#d9d7d2,#b8b2aa 45%,#3a3f52 85%);box-shadow:0 6px 18px rgba(0,0,0,.2)" role="img" aria-label="Video still: musician looking down beside a bright window"></div>
<svg class="abs" style="left:567px;top:1946px" width="64" height="64" viewBox="0 0 64 64"><circle cx="32" cy="32" r="31" fill="#2a2a2a" fill-opacity=".85"/><path d="M25 18 L47 32 L25 46 Z" fill="#fff"/></svg>
<div class="dot" style="left:560px;background:#444"></div>
<div class="dot" style="left:576px"></div>
<div class="dot" style="left:592px"></div>
<div class="dot" style="left:608px"></div>
<div class="dot" style="left:624px"></div>

<!-- TOURS -->
<section>
  <h2 class="abs" style="top:2420px;left:110px;font-family:'Oswald',sans-serif;font-weight:500;font-size:36px">TOURS</h2>
  <p class="abs tour-text">Nemo enim ipsam voluptatem quia volupt sit aspernatur aut odit aut fugit, sed quia conse quu ntur magni dolores eos qui ratione volup ttem se qui nesciunt. Neque porro quisquam est, qui dol orem ipsum quia dolor sit amet, consectetur, adi pisci velit, sed quia non num quam eius modi tile mpora incidunt ut labore et dolore magnjam ali quam quaerat voluatt odit aut fugit, sed quia cem.</p>
  <div class="ghost-word" style="left:535px;top:2828px;font-size:150px">Tours</div>

  <div class="tour-title" style="top:2412px">Ea Commodo Consequa</div>
  <div class="tour-meta" style="top:2452px">
    <svg width="14" height="13" viewBox="0 0 16 15"><rect x="1" y="2" width="14" height="12" fill="none" stroke="#666" stroke-width="1.6"/><rect x="1" y="2" width="14" height="3" fill="#666"/></svg>Mar 8, 2022 &nbsp;|&nbsp;
    <svg width="10" height="14" viewBox="0 0 10 14"><path d="M5 0 A5 5 0 0 1 10 5 C10 9 5 14 5 14 C5 14 0 9 0 5 A5 5 0 0 1 5 0 Z" fill="#666"/><circle cx="5" cy="5" r="2" fill="#fff"/></svg>Los Angeles, CA, USA
  </div>
  <div class="btn" style="left:770px;top:2495px;width:117px;height:48px">Tickets</div>
  <div class="btn" style="left:897px;top:2495px;width:117px;height:48px">Read More</div>

  <div class="tour-title" style="top:2575px">Ea Commodo Consequa</div>
  <div class="tour-meta" style="top:2615px">
    <svg width="14" height="13" viewBox="0 0 16 15"><rect x="1" y="2" width="14" height="12" fill="none" stroke="#666" stroke-width="1.6"/><rect x="1" y="2" width="14" height="3" fill="#666"/></svg>Mar 8, 2022 &nbsp;|&nbsp;
    <svg width="10" height="14" viewBox="0 0 10 14"><path d="M5 0 A5 5 0 0 1 10 5 C10 9 5 14 5 14 C5 14 0 9 0 5 A5 5 0 0 1 5 0 Z" fill="#666"/><circle cx="5" cy="5" r="2" fill="#fff"/></svg>San Jose, CA, USA
  </div>
  <div class="btn" style="left:770px;top:2658px;width:117px;height:48px">Tickets</div>
  <div class="btn" style="left:897px;top:2658px;width:117px;height:48px">Read More</div>

  <div class="tour-title" style="top:2738px">Ea Commodo Consequa</div>
  <div class="tour-meta" style="top:2778px">
    <svg width="14" height="13" viewBox="0 0 16 15"><rect x="1" y="2" width="14" height="12" fill="none" stroke="#666" stroke-width="1.6"/><rect x="1" y="2" width="14" height="3" fill="#666"/></svg>Mar 8, 2022 &nbsp;|&nbsp;
    <svg width="10" height="14" viewBox="0 0 10 14"><path d="M5 0 A5 5 0 0 1 10 5 C10 9 5 14 5 14 C5 14 0 9 0 5 A5 5 0 0 1 5 0 Z" fill="#666"/><circle cx="5" cy="5" r="2" fill="#fff"/></svg>Las Vegas, NV, USA
  </div>
  <div class="btn" style="left:770px;top:2821px;width:117px;height:48px">Tickets</div>
  <div class="btn" style="left:897px;top:2821px;width:117px;height:48px">Read More</div>

  <div class="abs view-all">View All Dates</div>
</section>

<!-- NEWS -->
<section class="news">
  <div class="ghost-word" style="left:-8px;top:690px;font-size:150px;color:#e2e2e2">News</div>
</section>
<h2 class="heading abs" style="top:3080px">News</h2>
<div class="photo" style="left:110px;top:3168px;width:313px;height:222px;background:linear-gradient(180deg,#9aa0a0,#5d6a60 45%,#2f3a33)" role="img" aria-label="Crowd with raised hands beneath dark trees and cloudy sky"></div>
<div class="photo" style="left:444px;top:3168px;width:312px;height:222px;background:radial-gradient(circle at 50% 45%,#b9bcc2,#5f646e 40%,#1c2030 75%)" role="img" aria-label="Silhouette of a grand piano against a large full moon"></div>
<div class="photo" style="left:777px;top:3168px;width:311px;height:222px;background:linear-gradient(180deg,#6a7382,#3b414c 50%,#1d2026)" role="img" aria-label="Concert crowd under stage lights"></div>
<div class="news-title" style="left:110px;top:3408px">Lorem ipsum dolor sit amet consec tetur adipiscing irure dolor</div>
<div class="news-title" style="left:444px;top:3408px">Lorem ipsum dolor sit amet consec tetur adipiscing irure dolor</div>
<div class="news-title" style="left:777px;top:3408px">Lorem ipsum dolor sit amet consec tetur adipiscing irure dolor</div>
<div class="news-date" style="left:110px;top:3485px">&#9635; Mar 8, 2022</div>
<div class="news-date" style="left:444px;top:3485px">&#9635; Mar 8, 2022</div>
<div class="news-date" style="left:777px;top:3485px">&#9635; Mar 8, 2022</div>
<div class="btn" style="left:527px;top:3553px;width:144px;height:61px;background:transparent">View More</div>

<!-- MERCH -->
<section>
  <div class="ghost-word" style="left:1075px;top:4202px;font-size:150px">Merch</div>
  <h2 class="heading abs" style="top:3768px">Merchandise!</h2>
  <div class="merch-box" style="left:110px"><div class="merch-photo" role="img" aria-label="Product photo: raglan long-sleeve tee"></div></div>
  <div class="merch-box" style="left:360px"><div class="merch-photo" role="img" aria-label="Product photo: black baseball cap"></div></div>
  <div class="merch-box" style="left:609px"><div class="merch-photo" role="img" aria-label="Product photo: silver water bottle"></div></div>
  <div class="merch-box" style="left:857px"><div class="merch-photo" role="img" aria-label="Product photo: grey baseball cap"></div></div>
  <div class="merch-name" style="left:110px">Lorem ipsua dolsit</div>
  <div class="merch-name" style="left:360px">Lorem ipsua dolsit</div>
  <div class="merch-name" style="left:609px">Lorem ipsua dolsit</div>
  <div class="merch-name" style="left:857px">Lorem ipsua dolsit</div>
  <div class="merch-price" style="left:110px">$35.00</div>
  <div class="merch-price" style="left:360px">$35.00</div>
  <div class="merch-price" style="left:609px">$35.00</div>
  <div class="merch-price" style="left:857px">$35.00</div>
  <div class="btn" style="left:514px;top:4266px;width:170px;height:59px">Visit The Store</div>
</section>

<!-- NEWSLETTER -->
<section class="newsletter" role="img" aria-label="Dim room with a piano and a seated figure">
  <div class="ghost-word" style="left:712px;top:250px;font-size:150px;color:#fff;opacity:.35;transform:none">Sign Up</div>
</section>
<h2 class="heading abs" style="top:4483px;color:var(--white)">Newsletter</h2>
<div class="field" style="left:228px;top:4562px;width:356px">Email Address</div>
<div class="field" style="left:612px;top:4562px;width:361px;display:flex;justify-content:space-between">Select Your Country
  <svg width="12" height="8" viewBox="0 0 12 8" style="margin-top:6px"><path d="M1 1 L6 6 L11 1" fill="none" stroke="#d8d8d8" stroke-width="1.5"/></svg>
</div>
<div class="btn" style="left:542px;top:4643px;width:116px;height:59px;background:#111;color:#fff;border-color:#fff">Submit</div>

<footer class="footer">© 2021 Tamsin Orlebo. Privacy Policy | Terms &amp; Conditions</footer>

</body>
</html>
```